Hunting Ethics Organization Needs a Web Design with Logo Refresh

This project involves the creation of a website design including the homepage design, inside page design, and logo refinements. Our organization is Talveth, and we are a not-for-profit hunting ethics organization.
The focus of the new website design is to bring attention the mission of our organization, provide an overview of the areas where our organization deploys its resources to support the modern hunter, and to encourage visitors to support our organization by donating in support of the organization’s mission.
The winning design will be implemented in Wordpress by our in-house team. If you have questions about how any particular design element may translate to Wordpress, please feel free to post questions in response to this brief. In general, however, we’re more focused on the evolution and delivery of a strong overall design aesthetic – we’ll shoulder the responsibility of how we translate that design into Wordpress.
See attached design brief for full details.
Hunting
2 page

```html
<!DOCTYPE html>
<html lang="en">
<head>
<meta charset="utf-8">
<title>Talveth — Protecting the Future of Hunting</title>
<link rel="stylesheet" href="https://fonts.googleapis.com/css2?family=Open+Sans:wght@400;600;700&display=swap">
<style>
:root{
  --blue:#0e4597;
  --blue-dark:#0b3a80;
  --orange:#f0a43a;
  --brown:#6a3a12;
  --cream:#fbf8ec;
  --text:#555;
  --text-light:#888;
  --footer:#e6e6e6;
  --white:#fff;
}
*{box-sizing:border-box;margin:0;padding:0}
html,body{width:910px;height:1200px;overflow:hidden}
body{font-family:"Open Sans",Arial,sans-serif;background:var(--white);position:relative;color:var(--text)}
.hero{position:absolute;left:0;top:0;width:910px;height:410px;background:linear-gradient(180deg,#c89a52 0%,#d9a552 35%,#b98338 70%,#8a5e2a 100%)}
.hero-photo{position:absolute;inset:0;background:radial-gradient(ellipse at 30% 40%,rgba(230,140,50,.55),rgba(0,0,0,0) 40%)}
.logo-badge{position:absolute;left:74px;top:0;width:163px;height:142px;z-index:3}
.logo-name{position:absolute;left:86px;top:26px;font-size:22px;font-weight:700;color:var(--blue);letter-spacing:.5px;z-index:4}
.logo-mark{position:absolute;left:86px;top:8px;width:14px;height:14px;border-radius:50%;background:var(--blue);z-index:4}
.logo-tag{position:absolute;left:83px;top:75px;font-size:6.5px;font-weight:600;color:var(--blue);letter-spacing:.5px;z-index:4}
.nav{position:absolute;left:237px;top:0;width:598px;height:54px;background:var(--blue);display:flex;align-items:center;padding-left:60px;gap:0}
.nav a{color:var(--white);text-decoration:none;font-size:9px;margin-right:28px}
.nav .donate{margin-left:auto;margin-right:15px;background:var(--orange);border-radius:14px;padding:8px 20px}
.slider-arrow{position:absolute;top:190px;width:28px;height:32px;background:rgba(80,80,80,.55);display:flex;align-items:center;justify-content:center}
.slider-arrow.prev{left:2px}.slider-arrow.next{right:2px}
.hero-list{position:absolute;left:406px;top:155px;list-style:none}
.hero-list li{display:flex;align-items:center;color:var(--white);font-size:18px;height:29px}
.hero-list svg{margin-right:10px}
.btn{position:absolute;top:252px;height:27px;border-radius:14px;color:var(--white);font-size:9px;font-weight:700;display:flex;align-items:center;justify-content:center}
.btn.involved{left:406px;width:119px;background:var(--blue)}
.btn.donation{left:534px;width:120px;background:var(--brown)}
.band{position:absolute;left:0;top:410px;width:910px;height:146px;background:var(--cream);border-bottom:1px solid #e4e2d8}
.card{position:absolute;top:370px;width:237px;height:148px;border:2px solid var(--white);box-shadow:0 10px 10px -8px rgba(0,0,0,.35)}
.card-photo{position:absolute;inset:0}
.card-label{position:absolute;left:0;bottom:0;width:132px;height:32px;background:var(--blue);color:var(--white);font-size:15px;display:flex;align-items:center;padding-left:13px}
.card-go{position:absolute;left:132px;bottom:0;width:31px;height:32px;background:var(--orange);color:var(--white);font-weight:700;font-size:12px;display:flex;align-items:center;justify-content:center}
.mission{position:absolute;left:0;top:584px;width:910px;text-align:center;font-size:20.5px;line-height:24px;color:#555}
.video{position:absolute;left:189px;top:649px;width:531px;height:212px;border-radius:3px;background:linear-gradient(90deg,#3e4a2c 0%,#c7441e 25%,#4a4a34 55%,#6d7a58 80%,#4c5238 100%)}
.play{position:absolute;left:248px;top:88px}
.divider{position:absolute;left:74px;top:894px;width:762px;height:1px;background:#e5e5e5}
.feature{position:absolute;top:926px;width:240px}
.feature h3{font-size:12px;font-weight:400;color:var(--blue);margin-bottom:6px}
.feature p{font-size:9.5px;line-height:14.5px;color:var(--text-light)}
.footer{position:absolute;left:0;top:1028px;width:910px;height:172px;background:var(--footer);border-bottom:2px solid var(--blue)}
.links{position:absolute;top:28px;list-style:none}
.links li{font-size:9.5px;color:#666;height:15.6px}
.vline{position:absolute;top:28px;width:1px;height:104px;background:#d3d3d3}
.footer h4{position:absolute;top:27px;font-size:10.5px;font-weight:600;color:#555;letter-spacing:.5px}
.signup{position:absolute;left:344px;top:55px;width:243px;height:31px;display:flex;border:1px solid #cfcfcf}
.signup .field{flex:1;background:var(--white);border-left:2px solid var(--blue);font-size:9px;color:#777;display:flex;align-items:center;padding-left:9px}
.signup .go{width:62px;background:var(--blue);color:var(--white);font-size:9.5px;font-weight:700;display:flex;align-items:center;justify-content:center}
.social{position:absolute;left:650px;top:57px;display:flex;gap:3px}
.social span{width:28px;height:28px;border:1.5px solid #777;border-radius:50%;display:block}
.copyright{position:absolute;left:0;top:136px;width:910px;text-align:center;font-size:8px;color:#666}
</style>
</head>
<body>
<section class="hero">
  <div class="hero-photo" role="img" aria-label="Hunter in orange gear with a shotgun walking through golden grass with a dog"></div>
  <div class="slider-arrow prev"><svg width="12" height="20"><path d="M10 1 2 10l8 9" stroke="#fff" stroke-width="1.6" fill="none"/></svg></div>
  <div class="slider-arrow next"><svg width="12" height="20"><path d="M2 1l8 9-8 9" stroke="#fff" stroke-width="1.6" fill="none"/></svg></div>
  <ul class="hero-list">
    <li><svg width="18" height="18"><path d="M9 1 17 9 9 17 1 9z" fill="#fff"/><path d="M5 9l3 3 6-6" stroke="#c99550" stroke-width="2" fill="none"/></svg>Protect the heritage of hunting</li>
    <li><svg width="18" height="18"><path d="M9 1 17 9 9 17 1 9z" fill="#fff"/><path d="M5 9l3 3 6-6" stroke="#c99550" stroke-width="2" fill="none"/></svg>Help us protect the future of hunting</li>
    <li><svg width="18" height="18"><path d="M9 1 17 9 9 17 1 9z" fill="#fff"/><path d="M5 9l3 3 6-6" stroke="#c99550" stroke-width="2" fill="none"/></svg>Support us as we empower the modern hunter</li>
  </ul>
  <div class="btn involved">GET INVOLVED</div>
  <div class="btn donation">MAKE A DONATION</div>
</section>

<svg class="logo-badge" viewBox="0 0 163 142"><path d="M0 0H163V96L81 142 0 96Z" fill="#fff"/></svg>
<div class="logo-mark"></div>
<div class="logo-name" style="left:106px;top:24px">Talveth</div>
<div class="logo-tag">PROTECTING THE FUTURE OF HUNTING</div>

<nav class="nav">
  <a>ABOUT US</a><a>HUNTING ETHICS</a><a>CONSERVATION</a><a>GET INVOLVED</a><a>CONTACT US</a>
  <a class="donate">DONATE</a>
</nav>

<div class="band"></div>
<div class="card" style="left:76px">
  <div class="card-photo" role="img" aria-label="Hunter kneeling and aiming a scoped rifle in a field" style="background:linear-gradient(180deg,#c9d3d9 0%,#b9ab7e 55%,#6e5a34 100%)"></div>
  <div class="card-label">Hunting Ethics</div><div class="card-go">»</div>
</div>
<div class="card" style="left:337px">
  <div class="card-photo" role="img" aria-label="Marsh landscape with a lookout tower at sunset" style="background:linear-gradient(180deg,#d8b8c8 0%,#b07a80 40%,#c2522c 70%,#9a4a28 100%)"></div>
  <div class="card-label">Conservation</div><div class="card-go">»</div>
</div>
<div class="card" style="left:598px">
  <div class="card-photo" role="img" aria-label="Father carrying his smiling son on his back outdoors" style="background:linear-gradient(90deg,#a7a08a 0%,#6a4a3a 45%,#e8e4e0 100%)"></div>
  <div class="card-label">Get Involved</div><div class="card-go">»</div>
</div>

<p class="mission">“Protecting the future of hunting as leaders in setting<br>the example for the modern hunter.”</p>

<div class="video" role="img" aria-label="Video still of a hunter in orange aiming at an elk in the forest">
  <svg class="play" width="36" height="36"><circle cx="18" cy="18" r="16.5" stroke="#fff" stroke-width="2" fill="rgba(0,0,0,.15)"/><path d="M14 11l10 7-10 7z" fill="#fff"/></svg>
</div>

<div class="divider"></div>
<div class="feature" style="left:74px"><h3>“ Sed ut perspiciatis unde omnis iste naer</h3><p>Aluptatem accusantium doloreloantium, trem ap eriam, eaque ipslorea quae aberitatecto bea tae vitae dicta sunt explicamo .</p></div>
<div class="feature" style="left:346px"><h3>“ Sed ut perspiciatis unde omnis iste naer</h3><p>Aluptatem accusantium doloreloantium, trem ap eriam, eaque ipslorea quae aberitatis ecto bea tae vitae dicta sunt explicamo .</p></div>
<div class="feature" style="left:615px"><h3>“ Sed ut perspiciatis unde os iste naer</h3><p>Aluptatem accusantium doloreloantium, trem ap eriam, eaque ipslorea quae aberiuitecto bea tae vitae dicta sunt explicamo .</p></div>

<footer class="footer">
  <ul class="links" style="left:75px"><li>Help</li><li>Contact Us</li><li>FAQ</li><li>Wholesale</li><li>Warranty</li></ul>
  <div class="vline" style="left:161px"></div>
  <ul class="links" style="left:195px;top:27px"><li>The Fine Print</li><li>Refunds &amp; Returns</li><li>Shipping</li><li>Privacy Policy</li><li>Terms &amp; Conditions</li></ul>
  <div class="vline" style="left:311px"></div>
  <h4 style="left:344px">NEWSLETTER: WE ONLY SEND GOOD THINGS.</h4>
  <div class="signup"><div class="field">Enter email Address:</div><div class="go">SIGN UP</div></div>
  <div class="vline" style="left:619px"></div>
  <h4 style="left:652px">FOLLOW US</h4>
  <div class="social"><span></span><span></span><span></span><span></span><span></span><span></span></div>
  <p class="copyright">Copyright ©2015 Talveth all rights reserved.terms and conditions and privacy policy</p>
</footer>
</body>
</html>
```